tam bor magazine

just need coupons of real customers made for my magazine, I have the layout or temp lets of the magazine i just need the coupons to be made and plug-in. i have examples, of the ads or coupons, I'm sure they will need to redone. and in a section of the magazine their in a church directory. with this section , i need the pic of the pastor plug in with their church information and in do have some ex-samples of that as well. with the websites of the businesses. if you need to grab an image from their site . you'll be able to do so. all of the business are in the upload section , these are small base business so a lot of the ads and logos need redone any way . so i will look at it and let you know.

P.S with the new coupons and logos I'm trying to impress these customers to stay with the magazine

Target Market(s)

small businesses

Requirements
Must have
• good graphics
Should not have
• not pixelated graphics

```html
<!DOCTYPE html>
<html lang="en">
<head>
<meta charset="utf-8">
<title>Church Directory</title>
<link rel="stylesheet" href="https://fonts.googleapis.com/css2?family=Anton&family=Oswald:wght@500;600;700&family=Source+Sans+3:wght@300;400;600&family=Poppins:wght@500;600;700&family=Roboto+Condensed:wght@400;700&family=Great+Vibes&display=swap">
<style>
:root{
  --ink:#111;
  --paper:#fff;
  --red:#d10d12;
  --deep-red:#a8070b;
  --gold:#ffd400;
  --phone-band:#efefaa;
  --photo-a:#e9e9e9;
  --photo-b:#cfcfcf;
}
*{box-sizing:border-box;margin:0;padding:0}
html,body{width:849px;height:1200px;overflow:hidden;background:var(--paper)}
.page{position:relative;width:849px;height:1200px;background:var(--paper);border:1px solid #222;font-family:"Source Sans 3",sans-serif;color:var(--ink)}

/* header */
.masthead{position:absolute;left:21px;top:18px;width:810px;height:130px;overflow:hidden;
  background:linear-gradient(180deg,#f2b28c 0%,#f08a6a 40%,#e9a07a 70%,#c98a6a 100%)}
.masthead-scene{position:absolute;inset:0;background:linear-gradient(90deg,rgba(255,255,255,.55) 0%,rgba(255,255,255,0) 22%),linear-gradient(0deg,rgba(80,50,40,.35) 0%,rgba(0,0,0,0) 25%)}
.masthead-title{position:absolute;left:0;top:0;width:810px;height:130px}

/* promo column */
.promo{position:absolute;left:21px;top:154px;width:260px;height:1019px;background:var(--paper);overflow:hidden}
.promo-host{position:absolute;left:0;top:0;width:260px;height:52px;background:#000;text-align:center;padding-top:10px;
  clip-path:polygon(0 0,100% 0,100% 88%,92% 92%,84% 86%,74% 94%,63% 88%,52% 95%,40% 87%,28% 94%,16% 88%,7% 95%,0 90%)}
.promo-host-name{font-family:"Poppins",sans-serif;font-weight:700;font-size:12.5px;color:var(--gold);letter-spacing:.1px}
.promo-host-tag{font-family:"Roboto Condensed",sans-serif;font-weight:700;font-size:6px;color:#fff;margin-top:1px}
.promo-present{position:absolute;left:0;top:62px;width:260px;text-align:center;font-family:"Poppins",sans-serif;font-weight:600;font-size:15px}
.promo-photo{position:absolute;left:0;top:72px;width:260px;height:262px;
  background:radial-gradient(circle at 50% 78%,#ffe680 0%,#f7a21a 20%,#e2701a 48%,#b8460e 80%,#8a2f08 100%);
  clip-path:polygon(0 12%,20% 9%,40% 11%,60% 7%,80% 10%,100% 2%,100% 96%,80% 98%,55% 95%,30% 99%,0 97%)}
.promo-title{position:absolute;left:0;top:0;width:260px;height:460px;font-family:"Anton",sans-serif;color:var(--red);font-weight:400;
  -webkit-text-stroke:1.4px #fff;paint-order:stroke fill;text-shadow:0 2px 2px rgba(0,0,0,.35);line-height:1}
.promo-title span{position:absolute;left:0;width:260px;text-align:center;display:block}
.promo-title .t1{top:296px;font-size:33px}
.promo-title .t2{top:318px;font-size:58px;letter-spacing:1px}
.promo-title .t3{top:367px;font-size:58px;letter-spacing:1.5px}
.promo-title .t4{top:421px;font-size:21px}
.promo-panel{position:absolute;left:0;top:455px;width:260px;height:564px;background:linear-gradient(180deg,#e00f14 0%,#c40a0e 60%,#a80609 100%);
  clip-path:polygon(0 3%,25% 2.4%,45% 1.2%,50% 0,60% 1.4%,82% 1.6%,94% .4%,100% 1.2%,100% 100%,0 100%)}
.symptoms-head{position:absolute;left:0;top:468px;width:260px;height:55px;background:var(--gold);
  display:flex;align-items:center;justify-content:center;font-family:"Oswald",sans-serif;font-weight:700;font-size:17px;letter-spacing:.2px;
  clip-path:polygon(0 10%,30% 6%,48% 0,66% 8%,100% 4%,100% 96%,70% 100%,40% 95%,0 100%)}
.symptoms-list{position:absolute;left:0;top:530px;width:260px;text-align:center;font-family:"Oswald",sans-serif;font-weight:600;font-size:12.5px;
  line-height:17.8px;color:#fff;text-shadow:1px 1px 0 #4a0000,-1px 0 0 #4a0000,0 -1px 0 #4a0000}
.promo-call{position:absolute;left:0;top:744px;width:260px;text-align:center;font-family:"Poppins",sans-serif;font-weight:700;font-size:18px;line-height:22.5px;color:#fff}
.promo-need{position:absolute;left:0;top:818px;width:260px;text-align:center;font-family:"Poppins",sans-serif;font-weight:600;font-size:13.5px;line-height:16px;color:#fff}
.event-date{position:absolute;left:36px;top:867px;width:200px;height:70px;color:#fff}
.event-date svg{position:absolute;left:0;top:10px}
.event-day{position:absolute;left:90px;top:0;font-family:"Poppins",sans-serif;font-weight:400;font-size:14px;white-space:nowrap}
.event-day span{color:var(--gold)}
.event-num{position:absolute;left:84px;top:10px;font-family:"Poppins",sans-serif;font-weight:700;font-size:46px;line-height:50px}
.event-time{position:absolute;left:90px;top:55px;font-family:"Poppins",sans-serif;font-weight:400;font-size:14px;white-space:nowrap}
.event-time span{color:var(--gold)}
.event-time b{font-weight:400;color:#fff;margin-left:8px}
.welcome-a{position:absolute;left:0;top:953px;width:260px;text-align:center;font-family:"Poppins",sans-serif;font-size:15px;color:var(--gold)}
.welcome-b{position:absolute;left:0;top:968px;width:260px;text-align:center;font-family:"Great Vibes",cursive;font-size:30px;color:#fff}

/* directory */
.directory{position:absolute;left:294px;top:155px;display:grid;grid-template-columns:264px 264px;grid-template-rows:repeat(5,194px);column-gap:8px;row-gap:12px}
.listing{position:relative;border:2px solid var(--ink);background:var(--paper)}
.listing-name{position:absolute;left:2px;right:2px;top:2px;height:44px;display:flex;align-items:center;justify-content:center;text-align:center;
  font-family:"Oswald",sans-serif;font-weight:600;font-size:17.5px;line-height:17px;letter-spacing:.1px}
.listing-name.two{font-size:16.5px}
.pastor-photo{position:absolute;left:14px;top:48px;width:100px;height:100px;border:1.5px solid #222;
  background:linear-gradient(160deg,var(--photo-a) 0%,var(--photo-b) 100%)}
.listing-info{position:absolute;left:118px;right:4px;top:50px;text-align:center}
.service{font-family:"Source Sans 3",sans-serif;font-weight:600;font-size:15px;line-height:17px}
.service.tight{font-size:13.8px;line-height:14px}
.service-extra{font-size:9.5px;line-height:10px;font-weight:400}
.address{font-family:"Source Sans 3",sans-serif;font-weight:300;font-size:9.3px;line-height:11.5px;margin-top:8px}
.address.caps{text-transform:uppercase}
.fine{font-family:"Roboto Condensed",sans-serif;font-size:6.6px;line-height:9.5px;text-transform:uppercase;margin-top:14px}
.fine.mixed{text-transform:none;font-size:7.3px;line-height:10px;margin-top:2px}
.pastor-name{position:absolute;left:4px;width:120px;top:157px;text-align:center;font-family:"Poppins",sans-serif;font-weight:600;font-size:11.2px;line-height:12px;text-transform:uppercase}
.pastor-name.cond{font-family:"Oswald",sans-serif;font-weight:600;font-size:10px;line-height:13px}
.phone-band{position:absolute;left:148px;right:2px;top:162px;height:15px;background:var(--phone-band);
  font-family:"Poppins",sans-serif;font-weight:600;font-size:13.5px;line-height:15px;padding-left:2px;white-space:nowrap}
.phone-band.two{height:auto;top:162px;font-family:"Oswald",sans-serif;font-size:9px;line-height:11px;background:linear-gradient(180deg,var(--phone-band) 0,var(--phone-band) 11px,transparent 11px)}
.phone-icon{position:absolute;left:119px;top:159px;width:23px;height:23px}
</style>
</head>
<body>
<div class="page">

  <header class="masthead">
    <div class="masthead-scene" role="img" aria-label="Sunset sky over a field with a white country church on the left"></div>
    <svg class="masthead-title" viewBox="0 0 810 130" aria-label="Church Directory">
      <rect x="404" y="22" width="6" height="90" fill="#b8683e"/>
      <rect x="387" y="36" width="40" height="5" fill="#b8683e"/>
      <text x="154" y="116" textLength="591" lengthAdjust="spacingAndGlyphs"
        font-family="Anton, sans-serif" font-size="104" fill="#d4080d" stroke="#fff" stroke-width="5" paint-order="stroke">CHURCH DIRECTORY</text>
    </svg>
  </header>

  <aside class="promo">
    <div class="promo-host">
      <div class="promo-host-name">MARLON AVERY MINISTRIES</div>
      <div class="promo-host-tag">HOUSE OF RESTORATION AND RENEWAL</div>
    </div>
    <div class="promo-present">PRESENT</div>
    <div class="promo-photo" role="img" aria-label="Silhouette with raised arms breaking chains against an orange sunset with birds"></div>
    <div class="promo-panel"></div>
    <h1 class="promo-title">
      <span class="t1">MID-WEEK</span>
      <span class="t2">INNER</span>
      <span class="t3">HEALING</span>
      <span class="t4">&amp; DELIVERANCE SERVICE</span>
    </h1>
    <div class="symptoms-head">SHORT LIST OF SYMPTOMS</div>
    <p class="symptoms-list">ABUSE, DEPRESSION, PTSD,<br>TRAUMA, WORRY, PANIC,<br>LONELINESS, SADNESS,<br>MOLESTATION, HEALTH ISSUES,<br>PAIN OR ILLNESS,<br>SUICIDAL THOUGHTS,<br>ADDICTIONS, CURSES,<br>HEARING STRANGE VOICES,<br>REJECTION, ANGER, FEAR,<br>ABANDONMENT, GUILT,<br>JEALOUSY, WORTHLESSNESS</p>
    <p class="promo-call">EXPERIENCED<br>OR SUFFERING<br>FROM 2 OR MORE</p>
    <p class="promo-need">YOU NEED SOME INNER<br>HEALING AND DELIVERANCE</p>
    <div class="event-date">
      <svg width="58" height="54" viewBox="0 0 58 54" fill="none" stroke="#ffd400" stroke-width="2.5">
        <rect x="12" y="6" width="43" height="40" rx="3"/>
        <line x1="12" y1="15" x2="55" y2="15"/>
        <line x1="20" y1="2" x2="20" y2="9"/><line x1="30" y1="2" x2="30" y2="9"/><line x1="40" y1="2" x2="40" y2="9"/><line x1="49" y1="2" x2="49" y2="9"/>
        <rect x="37" y="21" width="5" height="5"/><rect x="45" y="21" width="5" height="5"/>
        <rect x="37" y="29" width="5" height="5"/><rect x="45" y="29" width="5" height="5"/>
        <rect x="37" y="37" width="5" height="5"/><rect x="45" y="37" width="5" height="5"/>
        <circle cx="18" cy="35" r="15" fill="#c40a0e"/>
        <polyline points="18,26 18,35 24,40"/>
      </svg>
      <div class="event-day">SUNDAY <span>SEPT.</span></div>
      <div class="event-num">14TH</div>
      <div class="event-time"><span>5:00PM</span><b>2023</b></div>
    </div>
    <p class="welcome-a">Come as you are,</p>
    <p class="welcome-b">Walk ins welcome</p>
  </aside>

  <main class="directory">

    <article class="listing">
      <h2 class="listing-name">CEDAR ROCK INTERNATIONAL MIN.</h2>
      <div class="pastor-photo" role="img" aria-label="Portrait of the bishop"></div>
      <div class="listing-info">
        <p class="service">Sunday Worship<br>Service 10:30am</p>
        <p class="address">418 Hillcrest Dr,<br>Riverton, PA.</p>
      </div>
      <p class="pastor-name">Bishop Harold<br>Vance Mercer, Jr</p>
      <div class="phone-band">(412) 555 0141</div>
      <svg class="phone-icon" viewBox="0 0 24 24"><circle cx="12" cy="12" r="12" fill="#111"/><path d="M8.2 6.2l2 2.1-1.1 1.6c.8 1.7 2.1 3 3.8 3.9l1.6-1.1 2.1 2-1 1.9c-4.3-.4-8.2-4.3-8.6-8.6z" fill="#fff"/></svg>
    </article>

    <article class="listing">
      <h2 class="listing-name">BETHEL GROVE BAPTIST CHURCH</h2>
      <div class="pastor-photo" role="img" aria-label="Portrait of the pastor"></div>
      <div class="listing-info">
        <p class="service">Sunday Worship<br>Service 10:30am</p>
        <p class="address">5210 Maple Street<br>Riverton, PA 19077</p>
      </div>
      <p class="pastor-name">Dr. Thomas<br>L. Brandt</p>
      <div class="phone-band">(412) 555 0172</div>
      <svg class="phone-icon" viewBox="0 0 24 24"><circle cx="12" cy="12" r="12" fill="#111"/><path d="M8.2 6.2l2 2.1-1.1 1.6c.8 1.7 2.1 3 3.8 3.9l1.6-1.1 2.1 2-1 1.9c-4.3-.4-8.2-4.3-8.6-8.6z" fill="#fff"/></svg>
    </article>

    <article class="listing">
      <h2 class="listing-name">ST. MARK BAPTIST CHURCH</h2>
      <div class="pastor-photo" role="img" aria-label="Photo of the pastor preaching at a pulpit"></div>
      <div class="listing-info">
        <p class="service tight">Sunday Worship<br>Service 10:30am<br>Sunday School 8:30am</p>
        <p class="address caps">3402 Oak Ave.<br>Riverton, PA</p>
      </div>
      <p class="pastor-name">Pastor, Rev.<br>Linda Marsh</p>
      <div class="phone-band">(412) 555 0193</div>
      <svg class="phone-icon" viewBox="0 0 24 24"><circle cx="12" cy="12" r="12" fill="#111"/><path d="M8.2 6.2l2 2.1-1.1 1.6c.8 1.7 2.1 3 3.8 3.9l1.6-1.1 2.1 2-1 1.9c-4.3-.4-8.2-4.3-8.6-8.6z" fill="#fff"/></svg>
    </article>

    <article class="listing">
      <h2 class="listing-name two">NEW PATH CHRISTIAN<br>FELLOWSHIP</h2>
      <div class="pastor-photo" role="img" aria-label="Photo of the apostle and pastor couple"></div>
      <div class="listing-info">
        <p class="service tight">Sunday Worship<br>Service 11:000am</p>
        <p class="service-extra">Wed. Bible Study @ 7:30pm<br>Saturday Prayer at 9:00am</p>
        <p class="address">2915 Linden Street,<br>Riverton, PA.</p>
      </div>
      <p class="pastor-name cond">Apostle Gregory<br>&amp; Pastor Nina Hale</p>
      <div class="phone-band">(412) 555 0118</div>
      <svg class="phone-icon" viewBox="0 0 24 24"><circle cx="12" cy="12" r="12" fill="#111"/><path d="M8.2 6.2l2 2.1-1.1 1.6c.8 1.7 2.1 3 3.8 3.9l1.6-1.1 2.1 2-1 1.9c-4.3-.4-8.2-4.3-8.6-8.6z" fill="#fff"/></svg>
    </article>

    <article class="listing">
      <h2 class="listing-name two">ZION HILL COMMUNITY<br>MISSIONARY BAPTIST CHURCH</h2>
      <div class="pastor-photo" role="img" aria-label="Portrait of the reverend"></div>
      <div class="listing-info">
        <p class="fine">In-person Sunday worship<br>service 9:00am &amp; replay 6:00pm EST<br>Wednesday midweek only<br>Bible study: 2:00am - 1:00pm<br>Midweek corporate prayer: 6:00pm-7:00pm</p>
        <p class="address caps">1180 Ridgeview Avenue<br>Riverton, PA 19077</p>
      </div>
      <p class="pastor-name cond">Reverend Calvin<br>R. Whitfield</p>
      <div class="phone-band two">412.555.0126 - CHURCH<br>412-555-0127 - FAX</div>
      <svg class="phone-icon" viewBox="0 0 24 24"><circle cx="12" cy="12" r="12" fill="#111"/><path d="M8.2 6.2l2 2.1-1.1 1.6c.8 1.7 2.1 3 3.8 3.9l1.6-1.1 2.1 2-1 1.9c-4.3-.4-8.2-4.3-8.6-8.6z" fill="#fff"/></svg>
    </article>

    <article class="listing">
      <h2 class="listing-name">WORD HARBOR CHURCH</h2>
      <div class="pastor-photo" role="img" aria-label="Portrait of the pastor"></div>
      <div class="listing-info">
        <p class="service">Sunday Worship<br>Service 10:0am</p>
        <p class="address">906 N. Elmwood Ave,<br>Riverton, PA 19077</p>
      </div>
      <p class="pastor-name">Rev. Dr. Samuel<br>T. Burke Jr.</p>
      <div class="phone-band">(412) 555 0154</div>
      <svg class="phone-icon" viewBox="0 0 24 24"><circle cx="12" cy="12" r="12" fill="#111"/><path d="M8.2 6.2l2 2.1-1.1 1.6c.8 1.7 2.1 3 3.8 3.9l1.6-1.1 2.1 2-1 1.9c-4.3-.4-8.2-4.3-8.6-8.6z" fill="#fff"/></svg>
    </article>

    <article class="listing">
      <h2 class="listing-name">REDEMPTION BAPTIST CHURCH</h2>
      <div class="pastor-photo" role="img" aria-label="Photo of the pastor speaking at a wooden pulpit"></div>
      <div class="listing-info">
        <p class="service tight">Sunday Worship<br>Service 11:00am</p>
        <p class="address caps" style="margin-top:22px">640 Fairview Ave,<br>Riverton, PA</p>
      </div>
      <p class="pastor-name">Dr. Arthur<br>J. Benson Sr.</p>
      <div class="phone-band">(412) 555 0165</div>
      <svg class="phone-icon" viewBox="0 0 24 24"><circle cx="12" cy="12" r="12" fill="#111"/><path d="M8.2 6.2l2 2.1-1.1 1.6c.8 1.7 2.1 3 3.8 3.9l1.6-1.1 2.1 2-1 1.9c-4.3-.4-8.2-4.3-8.6-8.6z" fill="#fff"/></svg>
    </article>

    <article class="listing">
      <h2 class="listing-name two">GRACE TEMPLE CHURCH<br>RIVERTON (GTC-RVT)</h2>
      <div class="pastor-photo" role="img" aria-label="Photo of the reverend and his wife"></div>
      <div class="listing-info">
        <p class="service">Sunday Worship<br>Service 8:00am<br>&amp; 10:45am</p>
        <p class="address caps">4417 Cedar Street,<br>Riverton, PA. 19077</p>
      </div>
      <p class="pastor-name">Rev. Marcus<br>Dean Pryor</p>
      <div class="phone-band">(412) 555 0186</div>
      <svg class="phone-icon" viewBox="0 0 24 24"><circle cx="12" cy="12" r="12" fill="#111"/><path d="M8.2 6.2l2 2.1-1.1 1.6c.8 1.7 2.1 3 3.8 3.9l1.6-1.1 2.1 2-1 1.9c-4.3-.4-8.2-4.3-8.6-8.6z" fill="#fff"/></svg>
    </article>

    <article class="listing">
      <h2 class="listing-name">STILL WATERS CHURCH</h2>
      <div class="pastor-photo" role="img" aria-label="Black and white portrait of the pastor" style="background:linear-gradient(160deg,#dcdcdc,#9a9a9a)"></div>
      <div class="listing-info">
        <p class="service">Sunday Worship<br>Service 10:30am</p>
        <p class="address">2238 Birch Street<br>Riverton, PA 19077</p>
      </div>
      <p class="pastor-name">Pst. Edward<br>K. Nolan</p>
      <div class="phone-band">(412) 555 0109</div>
      <svg class="phone-icon" viewBox="0 0 24 24"><circle cx="12" cy="12" r="12" fill="#111"/><path d="M8.2 6.2l2 2.1-1.1 1.6c.8 1.7 2.1 3 3.8 3.9l1.6-1.1 2.1 2-1 1.9c-4.3-.4-8.2-4.3-8.6-8.6z" fill="#fff"/></svg>
    </article>

    <article class="listing">
      <h2 class="listing-name two">HOLLIS STREET MISSIONARY<br>BAPTIST CHURCH</h2>
      <div class="pastor-photo" role="img" aria-label="Portrait of the pastor"></div>
      <div class="listing-info">
        <p class="fine mixed">Church Service Join us Virtually<br>Sunday Academy 7:30am<br>Sunday Worship 9am, 2pm, 7pm, 10pm<br>Mondays 8am and 12 Noon<br>Wednesday at 12Noon<br>Saturdays at 10pm</p>
        <p class="address" style="margin-top:6px">7025 Hollis St.<br>Riverton, PA</p>
      </div>
      <p class="pastor-name">Rev. Dr. Vernon<br>L. Price</p>
      <div class="phone-band">(412) 555 0130</div>
      <svg class="phone-icon" viewBox="0 0 24 24"><circle cx="12" cy="12" r="12" fill="#111"/><path d="M8.2 6.2l2 2.1-1.1 1.6c.8 1.7 2.1 3 3.8 3.9l1.6-1.1 2.1 2-1 1.9c-4.3-.4-8.2-4.3-8.6-8.6z" fill="#fff"/></svg>
    </article>

  </main>
</div>
</body>
</html>
```